Brookmere Osteopathy flyer

I want a clean clear DL flyer (but also want an A4 poster) promoting a new Osteopathic business in a semi rural area in Tasmania (Australia).
It can have pictures like the examples attached to show people what Osteopathy is (its like Chiropractic and physiotherapy).
I am the sole practioner and am male, so any pictures would be best to be a white male if possible.
I've attached some wording, you can use all, or none of it
I don't have a phone number for the business yet
info@brookmereosteopathy.example
www.brookmereosteopathy.example
Target Market(s)
Australians, from tradies, professionals, babies to retired people
Industry/Entity Type
Health
Look and feel

```html
<!DOCTYPE html>
<html lang="en">
<head>
<meta charset="utf-8">
<title>Brookmere Osteopathy – DL Flyer</title>
<link rel="stylesheet" href="https://fonts.googleapis.com/css2?family=Lato:wght@400;700&display=swap">
<style>
  :root {
    --stage: #a3a3a3;
    --paper: #ffffff;
    --blue: #1b93d3;
    --blue-deep: #1580c0;
    --orange: #f3941f;
    --ink: #1d1d1d;
    --ink-soft: #333333;
  }
  * { margin: 0; padding: 0; box-sizing: border-box; }
  html, body { width: 1200px; height: 1200px; overflow: hidden; }
  body {
    background: var(--stage);
    font-family: "Lato", Arial, sans-serif;
    color: var(--ink);
  }
  .flyer {
    position: absolute;
    left: 348px; top: 65px;
    width: 504px; height: 1070px;
    background: var(--paper);
    overflow: hidden;
  }
  .flyer-art { position: absolute; inset: 0; }
  .brand {
    position: absolute;
    left: 300px; top: 92px;
    width: 150px;
    display: flex; flex-direction: column; align-items: center; gap: 8px;
    color: var(--blue);
    font-weight: 700;
    font-size: 19px;
    line-height: 1.15;
    text-align: center;
    letter-spacing: 0.5px;
  }
  .brand-dot {
    width: 18px; height: 18px;
    border-radius: 50%;
    background: var(--orange);
  }
  .reasons {
    position: absolute;
    left: 31px; top: 572px;
  }
  .reasons-title {
    font-size: 16px;
    font-weight: 700;
    color: var(--ink);
    margin-bottom: 14px;
  }
  .reasons-list {
    list-style: none;
    font-size: 13.4px;
    line-height: 17.3px;
    color: var(--ink-soft);
  }
  .reasons-list li { position: relative; padding-left: 34px; }
  .reasons-list li::before {
    content: "";
    position: absolute;
    left: 9px; top: 7px;
    width: 4px; height: 4px;
    border-radius: 50%;
    background: var(--ink);
  }
  .about {
    position: absolute;
    left: 31px; top: 832px;
    width: 240px;
    color: #ffffff;
    font-size: 13px;
    line-height: 17.4px;
  }
  .contacts {
    position: absolute;
    left: 31px; top: 952px;
    list-style: none;
    font-size: 13.4px;
    line-height: 22.5px;
    color: var(--ink-soft);
  }
  .contacts li { display: flex; align-items: center; gap: 9px; }
  .contacts svg { width: 10px; height: 10px; flex: none; }
</style>
</head>
<body>
  <main class="flyer">
    <svg class="flyer-art" viewBox="0 0 504 1070" width="504" height="1070" aria-hidden="false">
      <defs>
        <linearGradient id="skin-tone" x1="0" y1="0" x2="1" y2="1">
          <stop offset="0" stop-color="#f3dccd"/>
          <stop offset="0.6" stop-color="#e7bea5"/>
          <stop offset="1" stop-color="#d9a88c"/>
        </linearGradient>
        <radialGradient id="infant-tone" cx="0.55" cy="0.4" r="0.6">
          <stop offset="0" stop-color="#e9cdbf"/>
          <stop offset="0.55" stop-color="#c9dbe9"/>
          <stop offset="1" stop-color="#ffffff" stop-opacity="0"/>
        </radialGradient>
        <linearGradient id="clinic-tone" x1="0" y1="0" x2="1" y2="1">
          <stop offset="0" stop-color="#e9e4e0"/>
          <stop offset="0.5" stop-color="#cdb9ad"/>
          <stop offset="1" stop-color="#8a8f96"/>
        </linearGradient>
      </defs>

      <polygon class="photo-treatment" role="img" aria-label="Photo: practitioner's hands massaging a patient's shoulder"
        points="0,56 190,56 290,310 154,556 0,556" fill="url(#skin-tone)"/>

      <polygon class="hex hex-blue-large" points="36,360 115,206 303,206 390,360 303,516 115,516"
        fill="var(--blue)" opacity="0.88"/>

      <polygon class="hex hex-orange-edge" points="399,385 446,310 504,310 504,460 446,460" fill="var(--orange)"/>

      <rect class="photo-infant" role="img" aria-label="Photo: gentle cranial treatment of a sleeping infant"
        x="215" y="480" width="295" height="320" fill="url(#infant-tone)"/>

      <polygon class="hex hex-orange-small" points="305,850 325,812 365,812 385,850 365,888 325,888"
        fill="var(--orange)" opacity="0.85"/>

      <polygon class="photo-stretch" role="img" aria-label="Photo: practitioner stretching a patient's arm on a treatment table"
        points="300,782 504,782 504,1035 300,1035 265,972" fill="url(#clinic-tone)"/>

      <polygon class="band-about" points="0,825 285,825 312,873 285,922 0,922" fill="var(--blue)"/>

      <polygon class="hex hex-blue-bottom" points="265,1040 298,975 365,975 398,1040 365,1105 298,1105"
        fill="var(--blue)" opacity="0.9"/>
    </svg>

    <div class="brand">
      <span class="brand-dot"></span>
      <span class="brand-name">Brookmere<br>Osteopathy</span>
    </div>

    <section class="reasons">
      <h2 class="reasons-title">Common reasons people visit an osteopath:</h2>
      <ul class="reasons-list">
        <li>Back / neck pain</li>
        <li>Headaches / migraines</li>
        <li>Joint and muscle pain</li>
        <li>Pregnancy-related discomfort</li>
        <li>Disc related issues</li>
        <li>Sciatica</li>
        <li>Plantar fasciitis</li>
        <li>Tendonitis / Bursitis</li>
        <li>Adhesive capsulitis (frozen shoulder)</li>
        <li>Tennis / Golfers elbow</li>
      </ul>
    </section>

    <p class="about">Osteopaths use a combination of joint manipulation, targeted deep tissue massage and stretching to improve function, relieve pain and support the body's ability to heal itself.</p>

    <ul class="contacts">
      <li><svg viewBox="0 0 10 10"><path d="M5 0a3.5 3.5 0 0 0-3.5 3.5C1.5 6 5 10 5 10s3.5-4 3.5-6.5A3.5 3.5 0 0 0 5 0zm0 5a1.4 1.4 0 1 1 0-2.8A1.4 1.4 0 0 1 5 5z" fill="var(--orange)"/></svg>48 Quarry Lane, Brookmere</li>
      <li><svg viewBox="0 0 10 10"><path d="M2 0.5l1.8 2-1 1.2a6 6 0 0 0 3.5 3.5l1.2-1 2 1.8-1 1.5C4 9 1 6 0.5 1.5z" fill="var(--orange)"/></svg>Insert Phone Number</li>
      <li><svg viewBox="0 0 10 10"><circle cx="5" cy="5" r="4.5" fill="var(--orange)"/></svg>www.brookmereosteopathy.example</li>
      <li><svg viewBox="0 0 10 10"><rect x="0.5" y="2" width="9" height="6.5" rx="1" fill="var(--orange)"/></svg>info@brookmereosteopathy.example</li>
    </ul>
  </main>
</body>
</html>
```